I need a full PowerPoint template (with multiple slide options) for a new imaging center company - Lumora Medical Imaging. I have attached the Logo and Brand Identity here.

```html
<!DOCTYPE html>
<html lang="en">
<head>
<meta charset="utf-8">
<title>Lumora Medical Imaging – Presentation Template</title>
<link rel="stylesheet" href="https://fonts.googleapis.com/css2?family=Montserrat:wght@400;500;600;700;800&display=swap">
<style>
:root{
  --board:#e9e9e9;
  --ink:#1a1446;
  --navy:#173a78;
  --blue:#1565b0;
  --sky:#0a8fd3;
  --pale:#bfe2f5;
  --green:#3aa655;
  --teal:#23a5a0;
  --white:#ffffff;
  --text:#111111;
}
*{margin:0;padding:0;box-sizing:border-box}
html,body{width:1200px;height:1200px;overflow:hidden;background:var(--board);font-family:"Montserrat",sans-serif}
.board{position:relative;width:1200px;height:1200px}

/* brand lockup */
.brand{position:absolute;left:263px;top:127px;display:flex;align-items:center;gap:22px;color:var(--ink)}
.brand-dot{width:162px;height:162px;border-radius:50%;background:var(--blue)}
.brand-name{font-weight:700;line-height:1}
.brand-name .word{display:block;font-size:104px;letter-spacing:2px}
.brand-name .line{display:block;font-size:38px;letter-spacing:3px;margin-top:14px;text-align:center}

/* slides */
.slide{position:absolute;width:535px;height:301px;overflow:hidden;box-shadow:8px 12px 22px rgba(0,0,0,.35)}
.slide svg.art{position:absolute;inset:0;width:100%;height:100%}
.s1{left:56px;top:395px;background:var(--white)}
.s2{left:611px;top:395px;background:var(--white)}
.s3{left:56px;top:728px;background:linear-gradient(135deg,#173d7c 0%,#1a5ca4 60%,#1b73b8 100%)}
.s4{left:611px;top:728px;background:linear-gradient(135deg,#173d7c 0%,#1a5ca4 60%,#1b73b8 100%)}

.mini-brand{position:absolute;display:flex;align-items:center;gap:6px;font-weight:700;line-height:1}
.mini-brand .dot{border-radius:50%;background:var(--blue)}
.mini-brand .word{display:block}
.mini-brand .line{display:block;text-align:center}
.mini-brand.lg{left:31px;top:27px;color:var(--ink)}
.mini-brand.lg .dot{width:46px;height:46px}
.mini-brand.lg .word{font-size:27px;letter-spacing:.5px}
.mini-brand.lg .line{font-size:10px;margin-top:4px;letter-spacing:.5px}
.mini-brand.sm{left:22px;top:21px}
.mini-brand.sm .dot{width:27px;height:27px}
.mini-brand.sm .word{font-size:16px}
.mini-brand.sm .line{font-size:6px;margin-top:2px}
.mini-brand.dark{color:var(--ink)}
.mini-brand.light{color:var(--white)}
.mini-brand.light .dot{background:var(--white)}

.cover-title{position:absolute;left:0;right:0;top:131px;text-align:center;color:var(--text);font-weight:800;line-height:1}
.cover-title .main{display:block;font-size:33px;letter-spacing:.5px}
.cover-title .sub{display:block;font-size:20px;margin-top:4px}

.section-title{position:absolute;color:var(--white);font-weight:700;line-height:1}
.s2 .section-title{left:281px;top:18px;font-size:22px}
.s3 .section-title,.s4 .section-title{right:22px;top:26px;font-size:22px;letter-spacing:.5px}

.subtitle{position:absolute;left:42px;top:96px;font-size:21px;font-weight:700;color:var(--text)}
.bullets{position:absolute;left:42px;top:127px;list-style:none;font-size:7.3px;line-height:9.4px;color:var(--text);width:200px}
.bullets li{padding-left:5px;text-indent:-5px}
.bullets li::before{content:"• "}

.url,.page{position:absolute;bottom:14px;font-size:7.5px;letter-spacing:.2px}
.s1 .url{right:15px;color:var(--text)}
.s2 .url{left:19px;bottom:17px;color:var(--ink)}
.s2 .page{right:17px;bottom:17px;color:var(--white)}
.s3 .url,.s4 .url{left:19px;color:var(--white)}
.s3 .page,.s4 .page{right:17px;color:var(--white)}

.photo{position:absolute;left:0;top:70px;width:535px;height:196px;background:linear-gradient(90deg,#1d3a5e 0%,#3f6f99 45%,#8fb6d6 75%,#c9dcea 100%)}
</style>
</head>
<body>
<div class="board">

  <div class="brand">
    <div class="brand-dot"></div>
    <div class="brand-name"><span class="word">LUMORA</span><span class="line">— MEDICAL IMAGING —</span></div>
  </div>

  <!-- Cover slide -->
  <section class="slide s1">
    <svg class="art" viewBox="0 0 535 301" preserveAspectRatio="none" aria-hidden="true">
      <defs>
        <linearGradient id="c1band" x1="0" y1="0" x2="1" y2="0"><stop offset="0" stop-color="#1259a8"/><stop offset="1" stop-color="#1a7cc4"/></linearGradient>
        <linearGradient id="c1top" x1="0" y1="0" x2="1" y2="1"><stop offset="0" stop-color="#3aa655"/><stop offset=".5" stop-color="#0a8fd3"/><stop offset="1" stop-color="#1259a8"/></linearGradient>
      </defs>
      <path d="M380 0 L535 0 L535 112 C500 70 450 30 380 0Z" fill="url(#c1top)"/>
      <path d="M385 0 C440 20 495 60 535 100 L535 88 C495 50 445 18 400 0Z" fill="#fff"/>
      <path d="M0 183 C80 250 260 290 535 301 L0 301Z" fill="url(#c1band)"/>
      <path d="M0 205 C100 260 300 290 460 301 L0 301Z" fill="#0a8fd3"/>
      <path d="M0 212 C110 265 300 292 430 301 L0 301Z" fill="#fff" opacity=".9"/>
      <path d="M0 216 C110 268 300 294 420 301 L0 301Z" fill="#1565b0"/>
      <path d="M0 240 C140 285 320 298 535 301 L0 301Z" fill="#23a5a0" opacity=".7"/>
      <path d="M0 250 C140 292 320 300 535 301 L0 301Z" fill="#1559a6"/>
    </svg>
    <div class="mini-brand lg dark"><span class="dot"></span><span><span class="word">LUMORA</span><span class="line">— MEDICAL IMAGING —</span></span></div>
    <h1 class="cover-title"><span class="main">YOUR TITLE HERE</span><span class="sub">SUBTITLE HERE</span></h1>
    <span class="url">www.lumoramedical.com</span>
  </section>

  <!-- Content slide -->
  <section class="slide s2">
    <svg class="art" viewBox="0 0 535 301" preserveAspectRatio="none" aria-hidden="true">
      <defs>
        <linearGradient id="c2band" x1="0" y1="0" x2="1" y2="0"><stop offset="0" stop-color="#173a78"/><stop offset="1" stop-color="#1f6bb0"/></linearGradient>
        <linearGradient id="c2foot" x1="0" y1="0" x2="1" y2="0"><stop offset="0" stop-color="#3aa655"/><stop offset=".5" stop-color="#1a7cc4"/><stop offset="1" stop-color="#173a78"/></linearGradient>
      </defs>
      <path d="M155 0 L245 0 L262 60 C230 30 195 12 155 0Z" fill="#3aa655"/>
      <path d="M175 0 L250 0 L255 55 C230 28 205 12 175 0Z" fill="#1565b0"/>
      <path d="M244 0 L255 0 L262 60 L256 60Z" fill="#bfe2f5"/>
      <path d="M255 0 L535 0 L535 59 L262 59Z" fill="url(#c2band)"/>
      <path d="M0 160 C40 240 110 285 200 301 L0 301Z" fill="#bfe2f5" opacity=".55"/>
      <path d="M0 250 C60 285 140 300 200 301 L0 301Z" fill="#3aa655"/>
      <path d="M0 262 C60 292 130 301 180 301 L0 301Z" fill="#bfe2f5"/>
      <path d="M250 301 C380 290 480 270 535 250 L535 301Z" fill="#bfe2f5"/>
      <path d="M250 301 C380 294 480 280 535 266 L535 301Z" fill="url(#c2foot)"/>
    </svg>
    <div class="mini-brand sm dark"><span class="dot"></span><span><span class="word">LUMORA</span><span class="line">— MEDICAL IMAGING —</span></span></div>
    <h2 class="section-title">Section Title Here</h2>
    <h3 class="subtitle">Subtitle Here</h3>
    <ul class="bullets">
      <li>Your text goes here. Your text goes here. Your text goes here. Your text goes here. Your text goes here.</li>
      <li>Your text goes here. Your text goes here. Your text goes here.</li>
      <li>Your text goes here. Your text goes here. Your text goes here.</li>
      <li>Your text goes here. Your text goes here. Your text goes here.</li>
    </ul>
    <span class="url">www.lumoramedical.com</span>
    <span class="page">PAGE 01</span>
  </section>

  <!-- Section slide -->
  <section class="slide s3">
    <svg class="art" viewBox="0 0 535 301" preserveAspectRatio="none" aria-hidden="true">
      <path d="M0 301 C200 290 400 250 535 230 L535 301Z" fill="#3aa655"/>
      <path d="M60 301 C250 292 420 262 535 248 L535 301Z" fill="#23a5a0"/>
      <path d="M140 301 C300 294 440 272 535 262 L535 301Z" fill="#1a4f94"/>
    </svg>
    <div class="mini-brand sm light"><span class="dot"></span><span><span class="word">LUMORA</span><span class="line">— MEDICAL IMAGING —</span></span></div>
    <h2 class="section-title">SECTION TITLE HERE</h2>
    <span class="url">www.lumoramedical.com</span>
    <span class="page">PAGE 03</span>
  </section>

  <!-- Image slide -->
  <section class="slide s4">
    <div class="photo" role="img" aria-label="Photo: clinician reviewing brain scan images on monitors in an imaging reading room"></div>
    <svg class="art" viewBox="0 0 535 301" preserveAspectRatio="none" aria-hidden="true">
      <path d="M0 266 L535 266 L535 301 L0 301Z" fill="#1a4f94"/>
      <path d="M150 301 C300 290 430 262 535 255 L535 301Z" fill="#bfe2f5"/>
      <path d="M200 301 C330 294 450 272 535 266 L535 301Z" fill="#1a5aa2"/>
    </svg>
    <div class="mini-brand sm light"><span class="dot"></span><span><span class="word">LUMORA</span><span class="line">— MEDICAL IMAGING —</span></span></div>
    <h2 class="section-title">SECTION TITLE HERE</h2>
    <span class="url">www.lumoramedical.com</span>
    <span class="page">PAGE 04</span>
  </section>

</div>
</body>
</html>
```